Riverpeak Analytics needs new design business card

We are video surveillance and analytics software development company.
I am looking for a professional business card.
Our website is www.riverpeakanalytics.example.au
Please have a loo and get the feel for who we are and what we do.
I do not know what else to give you apart from good luck and I hope your design gets selected.
Thank you very much for participating
Business
Contact Information for Business Card
Address
27/15 Marlowe Street Fernbrook NSW 2199
Telephone 1300 582 417
Mobile 0450 731 258
email: marcus@riverpeakanalytics.example.au
name
Marcus Helvard
Position
Managing Director
Font styles to use
Other font styles liked:
- Arial
Look and feel

```html
<!DOCTYPE html>
<html lang="en">
<head>
<meta charset="utf-8">
<title>Riverpeak Analytics – Business Card</title>
<link rel="stylesheet" href="https://fonts.googleapis.com/css2?family=Open+Sans:wght@400;600;700&display=swap">
<style>
  :root {
    --backdrop: #e4e5e7;
    --navy: #0f3562;
    --navy-deep: #0a2748;
    --slate: #4b5b6c;
    --muted: #6f7b87;
    --orange: #f39a2b;
    --paper: #ffffff;
  }
  html, body {
    margin: 0;
    width: 1200px;
    height: 871px;
    overflow: hidden;
    background: var(--backdrop);
    font-family: "Open Sans", Arial, sans-serif;
  }
  .canvas {
    position: relative;
    width: 1200px;
    height: 871px;
  }
  .card {
    position: absolute;
    left: 290px;
    width: 620px;
    height: 354px;
    box-sizing: border-box;
    overflow: hidden;
    box-shadow: 0 6px 18px rgba(0,0,0,0.18);
  }
  /* Back side */
  .card-back {
    top: 60px;
    background: linear-gradient(160deg, var(--navy) 0%, var(--navy-deep) 100%);
    display: flex;
    align-items: center;
    justify-content: center;
    gap: 16px;
  }
  .brand-mark {
    width: 22px;
    height: 22px;
    background: var(--orange);
  }
  .back-lockup {
    display: flex;
    flex-direction: column;
    gap: 4px;
  }
  .back-name {
    color: var(--paper);
    font-weight: 600;
    font-size: 24px;
    letter-spacing: 0.5px;
  }
  .back-web {
    color: var(--orange);
    font-size: 13px;
  }
  /* Front side */
  .card-front {
    top: 457px;
    background: var(--paper);
  }
  .brand-name {
    position: absolute;
    left: 36px;
    top: 52px;
    margin: 0;
    color: var(--navy);
    font-weight: 700;
    font-size: 28px;
    line-height: 1;
    letter-spacing: 0.3px;
  }
  .contact {
    position: absolute;
    left: 300px;
    right: 28px;
    top: 104px;
    color: var(--muted);
    font-size: 13px;
    line-height: 1.45;
  }
  .person-name {
    margin: 0;
    color: var(--slate);
    font-weight: 700;
    font-size: 18px;
  }
  .person-role {
    margin: 0 0 12px;
    color: var(--orange);
    font-size: 13px;
  }
  .address { margin: 0 0 6px; }
  .contact-list {
    list-style: none;
    margin: 0;
    padding: 0;
  }
  .contact-list li {
    display: flex;
    align-items: center;
    gap: 12px;
    height: 22px;
    white-space: nowrap;
  }
  .contact-icon {
    width: 12px;
    height: 12px;
    flex: none;
  }
</style>
</head>
<body>
<main class="canvas">

  <section class="card card-back" aria-label="Card back">
    <span class="brand-mark"></span>
    <div class="back-lockup">
      <span class="back-name">Riverpeak Analytics</span>
      <span class="back-web">www.riverpeakanalytics.example.au</span>
    </div>
  </section>

  <section class="card card-front" aria-label="Card front">
    <h1 class="brand-name">Riverpeak Analytics</h1>

    <div class="contact">
      <p class="person-name">Marcus Helvard</p>
      <p class="person-role">Managing Director</p>
      <p class="address">Address 27/15 Marlowe Street<br>Fernbrook NSW 2199</p>
      <ul class="contact-list">
        <li>
          <svg class="contact-icon" viewBox="0 0 12 12" aria-hidden="true">
            <path d="M1 4 Q6 0 11 4 L9.5 5.5 L8 4.5 L8 3.6 Q6 3 4 3.6 L4 4.5 L2.5 5.5 Z" fill="none" stroke="#f39a2b" stroke-width="1"/>
            <rect x="2.5" y="6.5" width="7" height="4.5" rx="0.8" fill="none" stroke="#f39a2b" stroke-width="1"/>
          </svg>
          <span>1300 582 417</span>
        </li>
        <li>
          <svg class="contact-icon" viewBox="0 0 12 12" aria-hidden="true">
            <rect x="3" y="0.5" width="6" height="11" rx="1" fill="none" stroke="#f39a2b" stroke-width="1"/>
            <line x1="5" y1="9.5" x2="7" y2="9.5" stroke="#f39a2b" stroke-width="1"/>
          </svg>
          <span>0450 731 258</span>
        </li>
        <li>
          <svg class="contact-icon" viewBox="0 0 12 12" aria-hidden="true">
            <rect x="0.5" y="2.5" width="11" height="7" fill="none" stroke="#f39a2b" stroke-width="1"/>
            <polyline points="0.5,2.5 6,6.5 11.5,2.5" fill="none" stroke="#f39a2b" stroke-width="1"/>
          </svg>
          <span>marcus@riverpeakanalytics.example.au</span>
        </li>
      </ul>
    </div>
  </section>

</main>
</body>
</html>
```